Flyer Design - High Quality

*** Although this current job contest is listed as a ‘one-off contest’ we are also looking at working with a graphic designer long-term, which will include quite regular design work. So even though this is just a small job, if you want to & you do a good job on this, we would love to look at working with you on a regular basis.
* The winning designer will also get a freelance job designing another flyer in same design
Job Basics:
1. the design of a ….
Promotional corporate flyer - size = A4 - approx 6 or 7 pages.
*** The design will need to be extremely high quality/professional. Must be of a similar or better standard as the attached flyers – 1) Dell Warrick_Info Pack & 2) DrOwen Pellby
* Please view these flyers first to ensure you can create a flyer of similar or better quality before proceeding.
Specific Requirements:
1. high-quality, professional promotional flyer [size = A4 - for online use predominantly . I.e. not for printing necessarily] using the text, images and basic instructions outlined on the word document attached - 'Flyer_All talks in 1_guidelines'.
2. Examples of similar quality (good) designs = 1) Dell Warrick_Info Pack & 2) DrOwen Pellby
Background:
I am a motivational speaker on health, well-being and work-life balance. This flyer is to be used for promotional purposes when clients inquire about me speaking at their conference. Dell Warrick & Owen Pellby are speakers who do somewhat similar talks to me, and who have flyers that I really like.
Theme: My general theme is ‘health and well-being’ (we're a little bit more towards natural health and Eastern medicine, but don't want it too ‘eastern’ if you know what I mean).
Main Look & Feel … to be conveyed:
Professional / Corporate
Health, Vitality and happiness (fresh, modern and vital)
eye-catching / attention grabbing
* The design should represent a balance between highly sophisticated, professional and classy - corporate savvy - with a hint of 'natural health, Eastern wisdom and a general ‘high energy/fresh health and vitality feel'. While we would like the design to convey some aspect of ‘ natural/Eastern’ wisdom), we predominantly want to convey the idea of ‘modern’ health (i.e. fresh, modern and vital).
Colours:
We are open to your creative suggestions, but were generally thinking something along the lines of the colours in our corporate logo –
dark blue, aqua blue, grey – see logo (QEV_300kb.jpg) in attachments
- possibly with some bright green, orange etc if you think it might suit – to help give it the ‘natural health’ feel.
* Notes:
1. SAVING YOUR TIME: If you just want to start just doing a quickish design of the first 1-2 pages and submitting that (images for these pages attached - though use own images if you think they are better), then that’s fine. Then we can let you know if it is along the lines of something we like or not. This way, you can do something relatively quickly, without wasting too much time, if it is definitely not something we like. Hope that helps - we are always conscious of trying to make things good for you as a designer too.
2. Do not feel completely bound to the ideas suggested/asked for. Feel free to convey the basic ideas/keys but feel free to use/follow some of your own ideas/creative desires.
3. Any photos/images should be royalty free (or ask us if we want to pay for it) and not widely used or seen in the public domain - i.e. we don’t want people to have seen the photo/image elsewhere (within reason).
Thanks a lot and look forward to receiving your first design!
Cheers
Tobin
Predominantly corporates / business groups.
Graphic Designer

```html
<!DOCTYPE html>
<html lang="en">
<head>
<meta charset="utf-8">
<title>Work Smarter not Harder – Tobin Hale</title>
<link href="https://fonts.googleapis.com/css2?family=PT+Sans+Narrow:wght@400;700&display=swap" rel="stylesheet">
<style>
  :root {
    --aqua: #2fb8e6;
    --aqua-light: #5fd0f2;
    --aqua-deep: #1a9fd6;
    --navy: #1c3f7a;
    --ink: #3a3a3a;
    --grey: #8a8a8a;
    --white: #ffffff;
  }
  * { margin: 0; padding: 0; box-sizing: border-box; }
  html, body { width: 848px; height: 1200px; overflow: hidden; background: var(--white); }
  .flyer {
    position: relative; width: 848px; height: 1200px; overflow: hidden;
    font-family: "PT Sans Narrow", "Arial Narrow", sans-serif; background: var(--white);
  }
  .headline { position: absolute; top: 40px; left: 0; width: 100%; text-align: center; }
  .headline__title {
    font-size: 60px; font-weight: 700; line-height: 1; letter-spacing: -0.5px;
    background: linear-gradient(180deg, var(--aqua-light) 0%, var(--aqua-deep) 100%);
    -webkit-background-clip: text; background-clip: text; color: transparent;
  }
  .headline__aside { font-size: 44px; font-weight: 700; line-height: 1.15; color: var(--navy); margin-top: 4px; }
  .headline__promise { font-size: 29px; color: var(--navy); margin-top: 14px; }
  .band { position: absolute; top: 252px; left: 0; width: 848px; height: 610px; }
  .band svg { display: block; }
  .photo {
    position: absolute; top: 276px; left: 0; width: 580px; height: 380px;
    background: linear-gradient(135deg, #c9d2d6 0%, #8e9aa0 45%, #e6e2dc 100%);
  }
  .intro {
    position: absolute; top: 676px; left: 108px; width: 490px;
    color: var(--white); font-size: 27px; line-height: 1.25;
  }
  .intro::first-letter { font-size: 40px; }
  .benefits { position: absolute; top: 892px; left: 108px; width: 680px; }
  .benefits__lead { font-size: 27px; color: var(--navy); margin-bottom: 6px; }
  .benefits__list { list-style: none; font-size: 19.5px; color: var(--ink); line-height: 1.4; }
  .benefits__list li::before { content: "•"; color: var(--aqua); margin-right: 5px; }
  .testimonial { position: absolute; top: 1110px; left: 124px; width: 400px; font-style: italic; font-size: 12.5px; color: var(--ink); }
  .testimonial cite { display: block; margin: 10px 0 0 28px; font-size: 12.5px; }
  .brand { position: absolute; top: 1092px; left: 568px; width: 220px; text-align: center; }
  .brand__name { font-size: 40px; font-weight: 400; color: var(--navy); letter-spacing: 2px; line-height: 1; }
  .brand__tagline { font-size: 11.5px; color: var(--grey); letter-spacing: 0.6px; margin-top: 4px; }
</style>
</head>
<body>
<main class="flyer">
  <header class="headline">
    <h1 class="headline__title">Work Smarter not Harder</h1>
    <p class="headline__aside">(or Beat the 'Busyness' of Business)</p>
    <p class="headline__promise">how to do 20% more.&nbsp; in 20% less time … with 20% less stress</p>
  </header>

  <div class="band" aria-hidden="true">
    <svg width="848" height="610" viewBox="0 0 848 610">
      <defs>
        <linearGradient id="bandFill" x1="0" y1="0" x2="0" y2="1">
          <stop offset="0" stop-color="#2eb6e6"/>
          <stop offset="1" stop-color="#55c9ef"/>
        </linearGradient>
        <linearGradient id="sheetFill" x1="0" y1="0" x2="1" y2="0">
          <stop offset="0" stop-color="#ffffff"/>
          <stop offset="0.55" stop-color="#f4f4f4"/>
          <stop offset="1" stop-color="#bdbdbd"/>
        </linearGradient>
      </defs>
      <rect width="848" height="610" fill="url(#bandFill)"/>
      <path d="M660 0 C 640 200, 640 400, 610 610 L848 610 L848 0 Z" fill="url(#sheetFill)"/>
      <path d="M640 0 C 622 200, 622 400, 594 610" stroke="#1a9fd6" stroke-width="6" fill="none"/>
      <path d="M650 0 C 632 200, 632 400, 604 610" stroke="#7fd9f5" stroke-width="2" fill="none"/>
      <path d="M656 0 C 638 200, 636 400, 610 610" stroke="#1a9fd6" stroke-width="1.5" fill="none"/>
      <path d="M664 0 C 646 200, 644 400, 618 610" stroke="#5cc8ee" stroke-width="1" fill="none"/>
    </svg>
  </div>

  <div class="photo" role="img" aria-label="Photo of smiling businesspeople shaking hands across a meeting table"></div>

  <p class="intro">The most sought-after session on motivation, time management and productivity, A highly practical, ‘hands-on’ session that teaches people the 7 peak productivity practices of the world’s most successful individuals / businesspeople.</p>

  <section class="benefits">
    <h2 class="benefits__lead">Tobin is a great choice if you want…</h2>
    <ul class="benefits__list">
      <li>an industry leader who is highly entertaining, yet highly practical &amp; down to earth</li>
      <li>how to cultivate the ‘high performance state’ or ‘flow state’ to do more in less time</li>
      <li>to use (and control) technology (email, phones) to save massive time …&amp; stress</li>
      <li>the secrets of world leaders such as Rex Palmer, Warren Stoll &amp; Grant Mallory</li>
      <li>how to do 20% more.&nbsp; in 20% less time … with 20% less stress…guaranteed!</li>
    </ul>
  </section>

  <blockquote class="testimonial">
    “…the overwhelming response was that this session was the best and most interesting”
    <cite>Neil Harwood – Dept. of Learning, Jobs and Skills</cite>
  </blockquote>

  <div class="brand">
    <p class="brand__name">TOBIN HALE</p>
    <p class="brand__tagline">HEALTH WELLBEING WORK-LIFE BALANCE</p>
  </div>
</main>
</body>
</html>
```